Menu Design Project

We are a post colonial tavern serving craft beer, local wine and fine spirits. Our colors are black, copper and old brick. We are on a town square,...

Town

```html
<!DOCTYPE html>
<html lang="en">
<head>
<meta charset="utf-8">
<title>Tavern Menu</title>
<link rel="stylesheet" href="https://fonts.googleapis.com/css2?family=EB+Garamond:wght@500;600&family=PT+Serif:ital@0;1&display=swap">
<style>
:root{
  --page:#ffffff;
  --board:#373334;
  --copper:#a98a5e;
  --item:#cdbda9;
  --text:#ece8e3;
  --note:#ad9370;
  --price:#b8ab9c;
}
*{margin:0;padding:0;box-sizing:border-box}
html,body{width:1200px;height:1000px;overflow:hidden;background:var(--page)}
.menu{position:relative;width:1200px;height:1000px}
.board{position:absolute;left:37px;top:62px;width:1126px;height:876px;background:var(--board)}
.divider-v{position:absolute;top:62px;width:2px;height:876px;background:var(--copper)}
.divider-h{position:absolute;left:888px;width:250px;height:2px;background:var(--copper)}
.section-title{position:absolute;font-family:"EB Garamond",serif;font-weight:600;font-size:27px;color:var(--copper);text-align:center;letter-spacing:.3px;line-height:1}
.item{position:absolute}
.item-head{display:flex;align-items:baseline;font-family:"EB Garamond",serif;font-weight:500;font-size:15.5px;color:var(--item);line-height:18px}
.item-head .leader{flex:1;border-bottom:1px dotted var(--price);margin:0 2px 4px;min-width:10px}
.item-head .price{font-family:"PT Serif",serif;font-size:10px;color:var(--price)}
.item-desc{font-family:"PT Serif",serif;font-style:italic;font-size:9.6px;line-height:13px;color:var(--text);margin-top:1px}
.item-note{font-family:"PT Serif",serif;font-size:9.6px;line-height:13px;color:var(--note)}
.col-left .item{left:73px;width:228px}
.col-mid .item{left:347px;width:506px}
.col-right .item{left:896px;width:232px}
</style>
</head>
<body>
<div class="menu">
  <div class="board"></div>
  <div class="divider-v" style="left:324px"></div>
  <div class="divider-v" style="left:874px"></div>
  <div class="divider-h" style="top:363px"></div>
  <div class="divider-h" style="top:568px"></div>

  <section class="col-left">
    <h2 class="section-title" style="left:37px;width:288px;top:101px">HORS D’OEUVRES</h2>
    <div class="item" style="top:153px"><div class="item-head">Calamari<span class="leader"></span><span class="price">9</span></div><p class="item-desc">Tender squid lightly floured then deep-fried,<br>served with fresh lemon wedges and<br>marinara sauce.</p></div>
    <div class="item" style="top:223px"><div class="item-head">Coconut Shrimp<span class="leader"></span><span class="price">9</span></div><p class="item-desc">Six Jumbo Shrimp battered in coconut flakes<br>then deep-fried, served with fresh lemon wedges<br>and sweet chili sauce.</p></div>
    <div class="item" style="top:293px"><div class="item-head">Cajun Shrimp Nuggets<span class="leader"></span><span class="price">10</span></div><p class="item-desc">Several Gulf Shrimp battered in our homemade<br>Cajun Seasoning then deepfried, served with<br>fresh lemon wedges our Remoulade Sauce.</p></div>
    <div class="item" style="top:362px"><div class="item-head">Southwest Shrimp Skewers<span class="leader"></span><span class="price">10</span></div><p class="item-desc">6 Gulf Shrimp grilled to perfection in Garlic and<br>Butter, topped with homemade<br>Pico De Gallo and fresh lemon wedges.</p></div>
    <div class="item" style="top:431px"><div class="item-head">Chicken Wings<span class="leader"></span><span class="price">10</span></div><p class="item-desc">Marinated Chicken Wings deep-fried then<br>hand-tossed into your choice of our homemade<br>buffalo sauce, honey barbeque sauce,<br>Honey Chipotle or served Naked with freshly cut<br>carrots, celery and your choice of Sauce.</p></div>
    <div class="item" style="top:525px"><div class="item-head">Deep-Fried Pickles<span class="leader"></span><span class="price">8</span></div><p class="item-desc">A generous portion of pickles tossed in our<br>signature batter then deep-fried, served with<br>a ranch sauce.</p></div>
    <div class="item" style="top:594px"><div class="item-head">Mozzarella Sticks<span class="leader"></span><span class="price">8</span></div><p class="item-desc">Mozzarella cheese seasoned with Italian Herbs<br>then deep-fried and served with marinara sauce.</p></div>
    <div class="item" style="top:651px"><div class="item-head">Chips &amp; Pico<span class="leader"></span><span class="price">7</span></div><p class="item-desc">Fresh Corn Tortilla Chips with fresh homemade<br>Pico De Gallo.</p></div>
    <div class="item" style="top:708px"><div class="item-head">Fried Green Tomatoes<span class="leader"></span><span class="price">8</span></div><p class="item-desc">Vine Ripe Fried Green Tomatoes with a Pimento<br>Cheese base and sprinkled with Bacon.</p></div>
    <div class="item" style="top:765px"><div class="item-head">Loaded Southwest Fries<span class="leader"></span><span class="price">10</span></div><p class="item-desc">Creole Seasoned fries layered with Cheddar and<br>Parmesean, topped with Pico De Gallo, homemade<br>Remoulade and Ranch.</p><p class="item-note">(Add Chicken for $3* / Add Steak for $5*)<br>*Not Included in Trio Price</p></div>
    <div class="item" style="top:859px"><div class="item-head">Aldwin’s Signature Trio<span class="leader"></span><span class="price">20</span></div><p class="item-desc">Choose any of the above three full portioned fresh<br>Hors D’ouevres.</p></div>
  </section>

  <section class="col-mid">
    <h2 class="section-title" style="left:326px;width:548px;top:101px">‘ENTREES</h2>
    <div class="item" style="top:153px"><div class="item-head">Tavern BLT<span class="leader"></span><span class="price">6</span></div><p class="item-desc">Tennessee Bacon cooked to perfection served with a fresh tomato slice, lettuce and mayo spread on<br>sourdough bread mayonnaise. Served with your choice of side item.</p><p class="item-note">(Add Fried Green Tomatoes for $2)</p></div>
    <div class="item" style="top:229px"><div class="item-head">Cajun Shrimp Po’boy<span class="leader"></span><span class="price">12</span></div><p class="item-desc">Cajun breaded Gulf Shrimp served on a Hoagie Bun with fresh tomatoes, lettuce and Mayo. Covered with<br>a Cajun Remoulade Sauce and sprinkled with Creole Seasoning. Served with your choice of side item.</p></div>
    <div class="item" style="top:291px"><div class="item-head">Buttermilk Battered Chicken Tenders<span class="leader"></span><span class="price">12</span></div><p class="item-desc">Three Huge Chicken Tenders, breaded and battered then hand-tossed into your choice of our homemade<br>buffalo sauce, honey barbeque sauce, Honey Chipotle or served regular with your choice of sauce.<br>Served with your choice of side item.</p></div>
    <div class="item" style="top:366px"><div class="item-head">Aldwin’s Famous Reuben Sandwich<span class="leader"></span><span class="price">10</span></div><p class="item-desc">Corned Beef, Provolone cheese and sauerkraut served on rye bread with signature dressing.<br>Served with your choice of side item.</p></div>
    <div class="item" style="top:428px"><div class="item-head">Philly Cheesesteak<span class="leader"></span><span class="price">10</span></div><p class="item-desc">Mouthwatering Philly Cheesesteak grilled with peppers and onions with our signature dressing.<br>Served with your choice of side item.</p></div>
    <div class="item" style="top:489px"><div class="item-head">Chicken Sandwich<span class="leader"></span><span class="price">10</span></div><p class="item-desc">Grilled or Fried Chicken Breast served on a Kaiser Bun with Lettuce, Tomato and Mayo. Hand-tossed in your<br>choice of our homemade buffalo sauce, honey barbeque sauce, Honey Chipotle or served Naked with freshly<br>cut carrots, celery and your choice of Sauce. Served with your choice of side item.</p></div>
    <div class="item" style="top:564px"><div class="item-head">Caribbean Grouper Sandwich<span class="leader"></span><span class="price">14</span></div><p class="item-desc">Caribbean Grouper grilled or fried, served on a Kaiser Roll with Lettuce, Tomato and Mayo.<br>Served with your choice of side item.</p></div>
    <div class="item" style="top:626px"><div class="item-head">B&amp;B Steak and Onions*<span class="leader"></span><span class="price">14</span></div><p class="item-desc">Shoulder Top Blade Steak cooked to your preference. Topped with Sauteed Onions, Crispy Bacon Bits and<br>Bleu Cheese Crumbles. Served with your choice of side item.</p></div>
    <div class="item" style="top:689px"><div class="item-head">Aldwin’s Signature Tavern Burger*<span class="leader"></span><span class="price">10</span></div><p class="item-desc">Our fresh, never frozen burgers are 100% Black Angus Beef and are made to perfection with your choice<br>of cheddar, Swiss, American or Provolone Cheese, Juicy Bacon, your choices of Ketchup, Mustard or mayo<br>served on a bun with your choices of tomato, lettuce and onion. Served with your choice of side item.</p></div>
    <div class="item" style="top:763px"><div class="item-head">Veracruz Quesadilla<span class="leader"></span><span class="price">7</span></div><p class="item-desc">Wheat Tortilla grilled with melted cheese, onions and jalepeno peppers with a side of Pico De Gallo and Sour<br>Cream. Served with your choice of side item.</p><p class="item-note">(Add Chicken for $3 / Add Steak or Shrimp for $5)</p></div>
    <div class="item" style="top:838px"><div class="item-head">River City Nachos<span class="leader"></span><span class="price">11</span></div><p class="item-desc">Fresh Corn Tortilla Chips with fresh homemade Pico De Gallo, melted cheese, onions, jalepeno peppers.<br>Served with your choice of side item.</p><p class="item-note">(Add Chicken for $3 / Add Steak or Shrimp for $5)</p></div>
  </section>

  <section class="col-right">
    <h2 class="section-title" style="left:876px;width:274px;top:101px">FRESH GREENS</h2>
    <div class="item" style="top:153px"><div class="item-head">House Salad<span class="leader"></span><span class="price">8</span></div><p class="item-desc">A generous portion of iceberg &amp; romaine lettuce<br>with fresh diced tomatoes, onions and carrots with<br>your choice of Ranch, Bleu Cheese, Italian or<br>Balsamic Vinaigrette dressing.</p></div>
    <div class="item" style="top:236px"><div class="item-head">Caesar Salad<span class="leader"></span><span class="price">8</span></div><p class="item-desc">A generous portion of romaine lettuce sprinkled<br>with parmesan cheese, croutons with a side of<br>Caesar dressing.</p><p class="item-note">Add Grilled or Fried Chicken 3<br>Add Steak* or Shrimp 5</p></div>

    <h2 class="section-title" style="left:876px;width:274px;top:396px">WRAPS</h2>
    <div class="item" style="top:441px"><div class="item-head">Veggie Wrap<span class="leader"></span><span class="price">8</span></div><p class="item-desc">Romaine and Iceberg Lettuce, onions and tomato<br>wrapped in a wheat tortilla with the dressing of<br>your choice. Served with your choice of side item.</p><p class="item-note">Add Grilled or Fried Chicken 3<br>Add Steak*, Grouper or Shrimp 5.</p></div>

    <h2 class="section-title" style="left:876px;width:274px;top:611px">FRESH CATCH</h2>
    <div class="item" style="top:676px"><div class="item-head">Garlic Buttered</div><div class="item-head">Scallops<span class="leader"></span><span class="price">Market Price</span></div><p class="item-desc">Three Fresh Scallops grilled to perfection in butter<br>and served with a side of garlic butter.</p></div>
    <div class="item" style="top:757px"><div class="item-head">Fresh Fish of the Day*<span class="leader"></span><span class="price">Market Price</span></div><p class="item-desc">Ask about the fish of the day, brought in fresh and<br>served to perfection. Seasons vary for Amberjack,<br>Chilean Seabass, Black Grouper, Mahi, Redfish,<br>Red Snapper, Swordfish, Tuna or Canadian Salmon.</p></div>
    <div class="item" style="top:843px"><div class="item-head">Surf and Turf*<span class="leader"></span><span class="price">Market Price</span></div><p class="item-desc">Fresh Catch of the day, grilled in buttered<br>seasoning and served along with an eight ounce<br>Shoulder Top Blade Steak covered in onions.</p></div>
  </section>
</div>
</body>
</html>
```